PebbleLoop screens tidy up

We would like advice on how to better present the following home page and overview pages.

The existing website is functional, but the pages don't appear professionals and pleasing to the eye. We would specifically like feedback on alignment and padding of icons and text to make the screen more appealing and polished.

We are following the quartz design system.

Number of Pages Required

1 page

Font styles to use
Sans Serif
Other font styles liked:
• IBM Plex, Poppins

```html
<!DOCTYPE html>
<html lang="en">
<head>
<meta charset="utf-8">
<title>PebbleLoop – Home and Overview</title>
<link href="https://fonts.googleapis.com/css2?family=Barlow:wght@400;500;600;700&display=swap" rel="stylesheet">
<style>
  :root{
    --canvas:#dedede;
    --main-bg:#f4f4f4;
    --white:#ffffff;
    --orange:#f2922f;
    --orange-dark:#e8672a;
    --peach:#fdeedd;
    --field:#e7e7e7;
    --ink:#222222;
    --muted:#555555;
    --card-inner:#f3f3f3;
    --illustration:#e9eef4;
  }
  *{box-sizing:border-box;margin:0;padding:0}
  html,body{width:808px;height:1200px;overflow:hidden}
  body{background:var(--canvas);font-family:'Barlow',sans-serif;color:var(--ink);position:relative}
  .screen{position:absolute;left:36px;width:739px;background:var(--main-bg);overflow:hidden}
  .screen-home{top:31px;height:480px}
  .screen-overview{top:549px;height:614px}
  .abs{position:absolute}
  .sidebar{position:absolute;left:0;top:0;width:155px;height:100%;background:var(--white)}
  .brand{position:absolute;left:18px;top:11px;display:flex;align-items:center;gap:5px;height:23px}
  .brand-dot{width:20px;height:20px;border-radius:50%;background:var(--orange)}
  .brand-name{font-size:13.5px;font-weight:600;color:var(--ink);letter-spacing:-.2px}
  .nav-item{position:absolute;left:18px;width:120px;height:21px;display:flex;align-items:center;font-size:7.2px;font-weight:500}
  .nav-item svg{width:8px;height:8px;margin-left:8px;margin-right:11px;fill:var(--ink)}
  .nav-item.active{background:var(--peach)}
  .active-bar{position:absolute;left:150px;width:4px;height:21px;background:var(--orange);border-radius:2px}
  .side-heading{position:absolute;left:18px;font-size:7.8px;font-weight:700}
  .add-btn{position:absolute;left:122px;width:15px;height:15px;border-radius:50%;background:var(--peach);color:var(--orange-dark);font-size:8px;line-height:15px;text-align:center}
  .select{position:absolute;left:18px;width:120px;height:21px;background:var(--field);font-size:8.3px;color:#333;display:flex;align-items:center;justify-content:space-between;padding:0 8px}
  .select::after{content:"";border-left:3px solid transparent;border-right:3px solid transparent;border-top:3px solid #222}
  .page-title{position:absolute;left:172px;top:16px;width:547px;height:24px;background:var(--orange);color:var(--white);font-size:13.4px;padding-left:12px;line-height:24px}
  .label{position:absolute;left:173px;font-size:7.2px;font-weight:700}
  .card{position:absolute;background:var(--white);border-radius:2px}
  .hex{position:absolute;width:24px;height:24px}
  .h-xl{font-size:11.3px;font-weight:700;position:absolute;line-height:1.05}
  .small{font-size:5.7px;color:var(--muted);position:absolute}
  .stat{position:absolute;display:flex;align-items:center;gap:3px;font-size:11px;font-weight:700}
  .stat svg{width:14px;height:14px}
  .illustration{position:absolute;width:66px;height:66px;border-radius:50%;background:radial-gradient(circle at 50% 45%,#dbe8f5 0,var(--white) 70%);border:1px solid #ececec}
  .count{position:absolute;width:17px;height:17px;border-radius:50%;background:var(--orange);color:var(--white);font-size:10px;font-weight:700;text-align:center;line-height:17px;border:1.5px solid var(--white)}
  .btn{position:absolute;background:var(--orange);color:var(--white);font-size:5.7px;font-weight:700;display:flex;align-items:center;justify-content:center;border-radius:1px}
  .inner-card{position:absolute;top:8px;width:256px;height:112px;background:var(--card-inner)}
  .subtitle{position:absolute;font-size:7.2px;font-weight:600}
  .number{position:absolute;font-size:10.3px;font-weight:700}
</style>
</head>
<body>
<svg width="0" height="0" style="position:absolute">
  <defs>
    <linearGradient id="hexfill" x1="0" y1="0" x2="0" y2="1">
      <stop offset="0" stop-color="#f6a24c"/><stop offset="1" stop-color="#e8632a"/>
    </linearGradient>
    <symbol id="hex-chart" viewBox="0 0 24 24"><polygon points="12,1 22,6.5 22,17.5 12,23 2,17.5 2,6.5" fill="url(#hexfill)"/><path d="M7 7v10h10" stroke="#fff" stroke-width="1.2" fill="none"/><rect x="9" y="11" width="1.6" height="5" fill="#fff"/><rect x="12" y="9" width="1.6" height="7" fill="#fff"/><rect x="15" y="12" width="1.6" height="4" fill="#fff"/></symbol>
    <symbol id="hex-doc" viewBox="0 0 24 24"><polygon points="12,1 22,6.5 22,17.5 12,23 2,17.5 2,6.5" fill="url(#hexfill)"/><rect x="7.5" y="6" width="8" height="11" rx="1" fill="none" stroke="#fff" stroke-width="1.2"/><path d="M9.5 9h4M9.5 11.5h4M9.5 14h2" stroke="#fff" stroke-width="1"/><path d="M13 17l4-5" stroke="#fff" stroke-width="1.4"/></symbol>
    <symbol id="hex-list" viewBox="0 0 24 24"><polygon points="12,1 22,6.5 22,17.5 12,23 2,17.5 2,6.5" fill="url(#hexfill)"/><rect x="7" y="7" width="10" height="2.2" fill="#fff"/><rect x="7" y="10.8" width="10" height="2.2" fill="#fff"/><rect x="7" y="14.6" width="6" height="2.2" fill="#fff"/><path d="M15.5 14.5v3M14 16h3" stroke="#fff" stroke-width="1"/></symbol>
    <symbol id="tick" viewBox="0 0 16 16"><path d="M13 5.5A6 6 0 1 1 10.5 2.6" fill="none" stroke="#f2922f" stroke-width="1.6"/><path d="M5 7.5l3 3 6.5-7" fill="none" stroke="#f2922f" stroke-width="1.8"/></symbol>
    <symbol id="file" viewBox="0 0 16 16"><rect x="2" y="1.5" width="9" height="13" fill="none" stroke="#f2922f" stroke-width="1.2"/><path d="M4 5h5M4 7.5h5M4 10h3" stroke="#f2922f" stroke-width="1"/><path d="M9 14l5-6" stroke="#f2922f" stroke-width="1.6"/></symbol>
    <symbol id="i-home" viewBox="0 0 10 10"><path d="M5 1L0.5 5h1.5v4h2.2V6.5h1.6V9H8V5h1.5z"/></symbol>
    <symbol id="i-align" viewBox="0 0 10 10"><rect x="3" y="1" width="4" height="1.3"/><rect x="1" y="3.6" width="8" height="1.3"/><rect x="3" y="6.2" width="4" height="1.3"/><rect x="1" y="8.6" width="8" height="1.3"/></symbol>
    <symbol id="i-gear" viewBox="0 0 10 10"><path d="M4.2 0.5h1.6l.3 1.4 1.2.6 1.3-.7 1.1 1.1-.7 1.3.5 1.2 1.5.3v1.6l-1.5.3-.5 1.2.7 1.3-1.1 1.1-1.3-.7-1.2.5-.3 1.5H4.2l-.3-1.5-1.2-.5-1.3.7-1.1-1.1.7-1.3-.5-1.2L0 5.8V4.2l1.5-.3.5-1.2-.7-1.3 1.1-1.1 1.3.7 1.2-.6zM5 3.3A1.7 1.7 0 1 0 5 6.7 1.7 1.7 0 0 0 5 3.3z"/></symbol>
    <symbol id="i-list" viewBox="0 0 10 10"><rect x="0.5" y="1" width="2" height="2"/><rect x="3.5" y="1" width="6" height="2"/><rect x="0.5" y="4" width="2" height="2"/><rect x="3.5" y="4" width="6" height="2"/><rect x="0.5" y="7" width="2" height="2"/><rect x="3.5" y="7" width="6" height="2"/></symbol>
    <symbol id="i-copy" viewBox="0 0 10 10"><path d="M3 1h4.5v6H3z M1.5 3h1v5.5H6v1H1.5z" fill="none" stroke="#222" stroke-width=".9"/></symbol>
    <symbol id="i-road" viewBox="0 0 10 10"><path d="M3 1h4l2.5 8h-3.5L5.5 6.5h-1L4 9H.5z"/></symbol>
  </defs>
</svg>

<!-- Home screen -->
<section class="screen screen-home">
  <aside class="sidebar">
    <div class="brand"><span class="brand-dot"></span><span class="brand-name">PebbleLoop</span></div>
    <div class="nav-item active" style="top:52px"><svg><use href="#i-home"/></svg>Home</div>
    <div class="nav-item" style="top:72px"><svg><use href="#i-align"/></svg>All Alerts</div>
    <div class="nav-item" style="top:91px"><svg><use href="#i-gear"/></svg>Manage</div>
    <div class="side-heading" style="top:127px">Campaigns</div>
    <div class="add-btn" style="top:124px">+</div>
    <div class="select" style="top:148px">My Custom campaign</div>
    <div class="nav-item" style="top:179px"><svg><use href="#i-list"/></svg>Overview</div>
    <div class="nav-item" style="top:199px"><svg><use href="#i-copy"/></svg>Files &amp; HoneyTokens</div>
    <div class="nav-item" style="top:218px"><svg><use href="#i-road"/></svg>Resources</div>
    <div class="nav-item" style="top:237px"><svg><use href="#i-align"/></svg>Alerts</div>
    <div class="nav-item" style="top:256px"><svg><use href="#i-gear"/></svg>Settings</div>
    <div class="select" style="top:286px">Default campaign</div>
  </aside>
  <div class="active-bar" style="top:52px"></div>

  <div class="page-title">Home</div>

  <div class="label" style="top:62px">Teamspace</div>
  <div class="card" style="left:172px;top:78px;width:546px;height:58px">
    <div class="h-xl" style="left:13px;top:12px">Default</div>
    <div class="small" style="left:13px;top:35px">The default client is created as a part of your user account</div>
  </div>

  <div class="label" style="top:150px">Subscription Overview</div>
  <div class="label" style="top:150px;left:454px">Files &amp; HoneyTokens</div>
  <div class="card" style="left:172px;top:166px;width:265px;height:82px">
    <svg class="hex" style="left:13px;top:8px"><use href="#hex-chart"/></svg>
    <div class="h-xl" style="left:13px;top:39px">Starter Pack usage</div>
    <div class="small" style="left:13px;top:63px">0 files active out of 10 allowed</div>
  </div>
  <div class="card" style="left:454px;top:166px;width:264px;height:82px">
    <svg class="hex" style="left:13px;top:8px"><use href="#hex-doc"/></svg>
    <div class="small" style="left:42px;top:17px">Statics</div>
    <div class="stat" style="left:16px;top:49px"><svg><use href="#tick"/></svg>0</div>
    <div class="stat" style="left:165px;top:49px"><svg><use href="#file"/></svg>30</div>
  </div>

  <div class="label" style="top:262px">Campaigns</div>
  <div class="card" style="left:172px;top:277px;width:546px;height:128px">
    <div class="inner-card" style="left:7px">
      <div class="illustration" style="left:20px;top:17px" role="img" aria-label="Illustration of two people handing over a folder of files"></div>
      <div class="count" style="left:64px;top:67px">0</div>
      <div class="h-xl" style="left:96px;top:18px">My custom campaign</div>
      <div class="small" style="left:96px;top:38px">This is my custom campaign for finding</div>
      <div class="subtitle" style="left:96px;top:52px">Files and HoneyTokens</div>
      <div class="btn" style="left:95px;top:73px;width:101px;height:17px">Active since : Jul 25 2023 13:12</div>
    </div>
    <div class="inner-card" style="left:282px">
      <div class="illustration" style="left:20px;top:17px" role="img" aria-label="Illustration of a person working at a desk surrounded by charts"></div>
      <div class="count" style="left:64px;top:67px">0</div>
      <div class="h-xl" style="left:96px;top:18px">Default campaign</div>
      <div class="small" style="left:96px;top:38px">Define your own mission, or combine different</div>
      <div class="subtitle" style="left:96px;top:52px">Files and HoneyTokens</div>
      <div class="btn" style="left:95px;top:73px;width:101px;height:17px">Active since : Jul 20 2023 12:17</div>
    </div>
  </div>
</section>

<!-- Overview screen -->
<section class="screen screen-overview">
  <aside class="sidebar">
    <div class="brand"><span class="brand-dot"></span><span class="brand-name">PebbleLoop</span></div>
    <div class="nav-item" style="top:52px"><svg><use href="#i-home"/></svg>Home</div>
    <div class="nav-item" style="top:72px"><svg><use href="#i-align"/></svg>All Alerts</div>
    <div class="nav-item" style="top:91px"><svg><use href="#i-gear"/></svg>Manage</div>
    <div class="side-heading" style="top:127px">Campaigns</div>
    <div class="add-btn" style="top:124px">+</div>
    <div class="select" style="top:148px">My Custom campaign</div>
    <div class="nav-item active" style="top:179px"><svg><use href="#i-list"/></svg>Overview</div>
    <div class="nav-item" style="top:199px"><svg><use href="#i-copy"/></svg>Files &amp; HoneyTokens</div>
    <div class="nav-item" style="top:218px"><svg><use href="#i-road"/></svg>Resources</div>
    <div class="nav-item" style="top:237px"><svg><use href="#i-align"/></svg>Alerts</div>
    <div class="nav-item" style="top:256px"><svg><use href="#i-gear"/></svg>Settings</div>
    <div class="select" style="top:286px">Default campaign</div>
  </aside>
  <div class="active-bar" style="top:179px"></div>

  <div class="page-title">Overview</div>

  <div class="label" style="top:62px">Campaigns</div>
  <div class="card" style="left:172px;top:78px;width:546px;height:91px">
    <div class="illustration" style="left:19px;top:11px" role="img" aria-label="Illustration of two people handing over a folder of files"></div>
    <div class="count" style="left:63px;top:60px">0</div>
    <div class="h-xl" style="left:99px;top:30px">My custom campaign</div>
    <div class="small" style="left:99px;top:50px">This is my custom campaign for finding</div>
    <div class="btn" style="left:377px;top:35px;width:47px;height:18px">Confirm</div>
  </div>

  <div class="label" style="top:200px">Campaigns Organisation</div>
  <div class="card" style="left:172px;top:216px;width:546px;height:78px">
    <svg class="hex" style="left:11px;top:14px;width:25px;height:25px"><use href="#hex-list"/></svg>
    <div class="h-xl" style="left:43px;top:14px">Self-enabling Deliverables<br>Proprietary Limited</div>
    <div class="small" style="left:43px;top:41px">Standard</div>
    <div class="number" style="left:43px;top:52px">86</div>
    <div class="h-xl" style="left:293px;top:14px">Unleash bleeding-edge mindshare</div>
    <div class="small" style="left:293px;top:41px">8 hours ago</div>
    <div class="number" style="left:293px;top:52px">8</div>
  </div>

  <div class="label" style="top:335px">Files &amp; HoneyTokens</div>
  <div class="label" style="top:335px;left:454px">Resources</div>
  <div class="card" style="left:172px;top:351px;width:265px;height:82px">
    <svg class="hex" style="left:13px;top:7px"><use href="#hex-doc"/></svg>
    <div class="small" style="left:42px;top:17px">Statics</div>
    <div class="stat" style="left:16px;top:48px"><svg><use href="#tick"/></svg>0</div>
    <div class="stat" style="left:165px;top:48px"><svg><use href="#file"/></svg>30</div>
  </div>
  <div class="card" style="left:453px;top:351px;width:265px;height:82px">
    <svg class="hex" style="left:13px;top:7px"><use href="#hex-chart"/></svg>
    <div class="small" style="left:47px;top:12px;line-height:11.5px">Generate a Collection of fictional organisations,<br>Custom templetes, Upload files and logos.</div>
  </div>

  <div class="label" style="top:466px">Alerts</div>
  <div class="card" style="left:172px;top:482px;width:265px;height:81px">
    <svg class="hex" style="left:13px;top:7px"><use href="#hex-doc"/></svg>
    <div class="small" style="left:42px;top:17px">Alert statics will appear here</div>
  </div>
</section>
</body>
</html>
```